Bluewren Business Cards

Name Tomas Velikor
Title Mortgage Originator
Phone (800) 641-2705 x32
Direct (571) 362-8104
Email tvelikor@bluewrenhomeloans.example
NMLS #3804427
Name Lien Vo
Title Mortgage Originator
Location (800) 641-2705 x55
Direct (440) 296-5081
Email lvo@bluewrenhomeloans.example
NMLS #3719046
Name Solomon Ked-Ravi
Title Mortgage Originator
Location (800) 641-2705 x56
Direct (202) 374-6019
Email skedravi@bluewrenhomeloans.example
NMLS #3748510
Name Roselle Dunfield
Title Mortgage Originator
Location (800) 641-2705 x57
Direct (240) 538-2274
Email rdunfield@bluewrenhomeloans.example
NMLS #3692384
Name Dana Whitcombe
Title Mortgage Originator
Location (800) 641-2705 x58
Direct (540) 681-3926
Email dwhitcombe@bluewrenhomeloans.example
NMLS #3657019
Name Idris Holt
Title Mortgage Originator
Location (800) 641-2705 x59
Direct (240) 163-8852
Email iholt@bluewrenhomeloans.example
NMLS #3781462
Name Zora Lund
Title Mortgage Originator
Location (800) 641-2705 x60
Direct (202) 449-2637
Email zora@zorafindshomes.example
NMLS #3795038
Contact Information for Business Card
Name Tomas Velikor Title Mortgage Originator Phone (800) 641-2705 x32 Direct (571) 362-8104 Email tvelikor@bluewrenhomeloans.example NMLS #3804427 Name Lien Vo Title Mortgage Originator Location (800) 641-2705 x55 Direct (440) 296-5081 Email lvo@bluewrenhomeloans.example NMLS #3719046 Name Solomon Ked-Ravi Title Mortgage Originator Location (800) 641-2705 x56 Direct (202) 374-6019 Email skedravi@bluewrenhomeloans.example NMLS #3748510 Name Roselle Dunfield Title Mortgage Originator Location (800) 641-2705 x57 Direct (240) 538-2274 Email rdunfield@bluewrenhomeloans.example NMLS #3692384 Name Dana Whitcombe Title Mortgage Originator Location (800) 641-2705 x58 Direct (540) 681-3926 Email dwhitcombe@bluewrenhomeloans.example NMLS #3657019 Name Idris Holt Title Mortgage Originator Location (800) 641-2705 x59 Direct (240) 163-8852 Email iholt@bluewrenhomeloans.example NMLS #3781462 Name Zora Lund Title Mortgage Originator Location (800) 641-2705 x60 Direct (202) 449-2637 Email zora@zorafindshomes.example NMLS #3795038

```html
<!DOCTYPE html>
<html lang="en">
<head>
<meta charset="utf-8">
<title>Bluewren Business Cards</title>
<link rel="stylesheet" href="https://fonts.googleapis.com/css2?family=Oswald:wght@600&family=Roboto+Condensed:wght@400;700&display=swap">
<style>
  :root{
    --backdrop:#000;
    --card:#ffffff;
    --brand-blue:#0d5e8d;
    --name-blue:#0b5a8c;
    --sky:#3b9fdc;
    --gold:#e3b04b;
    --panel-text:#ffffff;
    --rule:rgba(255,255,255,.75);
  }
  *{box-sizing:border-box;margin:0;padding:0}
  html,body{width:1200px;height:745px;overflow:hidden;background:var(--backdrop)}
  .sheet{position:relative;width:1200px;height:745px}
  .card{position:absolute;width:350px;height:203px;background:var(--card);overflow:hidden}
  .portrait{position:absolute;left:0;top:0;width:170px;height:203px}
  .brand{position:absolute;left:178px;top:22px;display:flex;align-items:center;gap:6px;
    font-family:"Roboto Condensed",sans-serif;font-weight:700;font-size:20px;color:var(--brand-blue)}
  .brand-dot{width:18px;height:18px;border-radius:50%;background:var(--gold)}
  .name{position:absolute;left:172px;top:71px;font-family:"Oswald",sans-serif;font-weight:600;
    font-size:18.5px;letter-spacing:.2px;color:var(--name-blue);white-space:nowrap}
  .title{position:absolute;left:172px;top:93px;font-family:"Roboto Condensed",sans-serif;
    font-size:16px;color:var(--name-blue);white-space:nowrap}
  .stripe-sky{position:absolute;left:172px;right:0;top:117px;height:2px;background:var(--sky)}
  .stripe-gold{position:absolute;left:172px;right:0;top:121px;height:4px;background:var(--gold)}
  .contact{position:absolute;left:172px;right:0;top:127px;bottom:0;background:var(--brand-blue);
    padding:5px 6px 0 8px;font-family:"Roboto Condensed",sans-serif;color:var(--panel-text)}
  .phone{font-size:12px;line-height:15.5px;white-space:nowrap}
  .divider{height:1px;background:var(--rule);margin:4px 12px 5px 0}
  .email{font-size:8.3px;line-height:14px;white-space:nowrap;letter-spacing:0}
  .nmls{font-size:11.5px;line-height:15px;white-space:nowrap}
</style>
</head>
<body>
<main class="sheet">

  <article class="card" style="left:63px;top:37px">
    <svg class="portrait" viewBox="0 0 170 203" role="img" aria-label="Portrait photo of Lien Vo">
      <defs><linearGradient id="g1" x1="0" y1="0" x2="0" y2="1"><stop offset="0" stop-color="#9a8c80"/><stop offset="1" stop-color="#2b3b55"/></linearGradient></defs>
      <path d="M0 0H108A48 101.5 0 0 1 108 203H0Z" fill="url(#g1)"/>
    </svg>
    <div class="brand"><span class="brand-dot"></span>Bluewren</div>
    <h2 class="name">LIEN VO</h2>
    <p class="title">Mortgage Originator</p>
    <div class="stripe-sky"></div><div class="stripe-gold"></div>
    <div class="contact">
      <p class="phone">(800) 641-2705 x55</p>
      <p class="phone">Direct (440) 296-5081</p>
      <div class="divider"></div>
      <p class="email">lvo@bluewrenhomeloans.example</p>
      <p class="nmls">NMLS #3719046</p>
    </div>
  </article>

  <article class="card" style="left:440px;top:37px">
    <svg class="portrait" viewBox="0 0 170 203" role="img" aria-label="Portrait photo of Dana Whitcombe">
      <defs><linearGradient id="g2" x1="0" y1="0" x2="0" y2="1"><stop offset="0" stop-color="#a08a78"/><stop offset="1" stop-color="#2a2a2e"/></linearGradient></defs>
      <path d="M0 0H108A48 101.5 0 0 1 108 203H0Z" fill="url(#g2)"/>
    </svg>
    <div class="brand"><span class="brand-dot"></span>Bluewren</div>
    <h2 class="name">DANA WHITCOMBE</h2>
    <p class="title">Mortgage Originator</p>
    <div class="stripe-sky"></div><div class="stripe-gold"></div>
    <div class="contact">
      <p class="phone">(800) 641-2705 x58</p>
      <p class="phone">Direct (540) 681-3926</p>
      <div class="divider"></div>
      <p class="email">Email dwhitcombe@bluewrenhomeloans.example</p>
      <p class="nmls">NMLS #3657019</p>
    </div>
  </article>

  <article class="card" style="left:813px;top:37px">
    <svg class="portrait" viewBox="0 0 170 203" role="img" aria-label="Portrait photo of Tomas Velikor">
      <defs><linearGradient id="g3" x1="0" y1="0" x2="0" y2="1"><stop offset="0" stop-color="#f4f4f2"/><stop offset="1" stop-color="#9cc98a"/></linearGradient></defs>
      <path d="M0 0H108A48 101.5 0 0 1 108 203H0Z" fill="url(#g3)"/>
    </svg>
    <div class="brand"><span class="brand-dot"></span>Bluewren</div>
    <h2 class="name">TOMAS VELIKOR</h2>
    <p class="title">Mortgage Originator</p>
    <div class="stripe-sky"></div><div class="stripe-gold"></div>
    <div class="contact">
      <p class="phone">(800) 641-2705 x32</p>
      <p class="phone">Direct (571) 362-8104</p>
      <div class="divider"></div>
      <p class="email">Email tvelikor@bluewrenhomeloans.example</p>
      <p class="nmls">NMLS #3804427</p>
    </div>
  </article>

  <article class="card" style="left:63px;top:265px">
    <svg class="portrait" viewBox="0 0 170 203" role="img" aria-label="Portrait photo of Solomon Ked-Ravi">
      <defs><linearGradient id="g4" x1="0" y1="0" x2="0" y2="1"><stop offset="0" stop-color="#34486a"/><stop offset="1" stop-color="#5a3438"/></linearGradient></defs>
      <path d="M0 0H108A48 101.5 0 0 1 108 203H0Z" fill="url(#g4)"/>
    </svg>
    <div class="brand"><span class="brand-dot"></span>Bluewren</div>
    <h2 class="name">SOLOMON KED-RAVI</h2>
    <p class="title">Mortgage Originator</p>
    <div class="stripe-sky"></div><div class="stripe-gold"></div>
    <div class="contact">
      <p class="phone">(800) 641-2705 x56</p>
      <p class="phone">Direct (202) 374-6019</p>
      <div class="divider"></div>
      <p class="email">Email skedravi@bluewrenhomeloans.example</p>
      <p class="nmls">NMLS #3748510</p>
    </div>
  </article>

  <article class="card" style="left:440px;top:265px">
    <svg class="portrait" viewBox="0 0 170 203" role="img" aria-label="Portrait photo of Idris Holt">
      <defs><linearGradient id="g5" x1="0" y1="0" x2="0" y2="1"><stop offset="0" stop-color="#d8cfc0"/><stop offset="1" stop-color="#22336b"/></linearGradient></defs>
      <path d="M0 0H108A48 101.5 0 0 1 108 203H0Z" fill="url(#g5)"/>
    </svg>
    <div class="brand"><span class="brand-dot"></span>Bluewren</div>
    <h2 class="name">IDRIS HOLT</h2>
    <p class="title">Mortgage Originator</p>
    <div class="stripe-sky"></div><div class="stripe-gold"></div>
    <div class="contact">
      <p class="phone">(800) 641-2705 x59</p>
      <p class="phone">Direct (240) 163-8852</p>
      <div class="divider"></div>
      <p class="email">Email iholt@bluewrenhomeloans.example</p>
      <p class="nmls">NMLS #3781462</p>
    </div>
  </article>

  <article class="card" style="left:63px;top:494px">
    <svg class="portrait" viewBox="0 0 170 203" role="img" aria-label="Portrait photo of Roselle Dunfield">
      <defs><linearGradient id="g6" x1="0" y1="0" x2="0" y2="1"><stop offset="0" stop-color="#ffffff"/><stop offset="1" stop-color="#e6a9b4"/></linearGradient></defs>
      <path d="M0 0H108A48 101.5 0 0 1 108 203H0Z" fill="url(#g6)"/>
    </svg>
    <div class="brand"><span class="brand-dot"></span>Bluewren</div>
    <h2 class="name">ROSELLE DUNFIELD</h2>
    <p class="title">Mortgage Originator</p>
    <div class="stripe-sky"></div><div class="stripe-gold"></div>
    <div class="contact">
      <p class="phone">(800) 641-2705 x57</p>
      <p class="phone">Direct (240) 538-2274</p>
      <div class="divider"></div>
      <p class="email">Email rdunfield@bluewrenhomeloans.example</p>
      <p class="nmls">NMLS #3692384</p>
    </div>
  </article>

  <article class="card" style="left:440px;top:494px">
    <svg class="portrait" viewBox="0 0 170 203" role="img" aria-label="Portrait photo of Zora Lund">
      <defs><linearGradient id="g7" x1="0" y1="0" x2="0" y2="1"><stop offset="0" stop-color="#d9d9d9"/><stop offset="1" stop-color="#f2f0ed"/></linearGradient></defs>
      <path d="M0 0H108A48 101.5 0 0 1 108 203H0Z" fill="url(#g7)"/>
    </svg>
    <div class="brand"><span class="brand-dot"></span>Bluewren</div>
    <h2 class="name">ZORA LUND</h2>
    <p class="title">Mortgage Originator</p>
    <div class="stripe-sky"></div><div class="stripe-gold"></div>
    <div class="contact">
      <p class="phone">(800) 641-2705 x60</p>
      <p class="phone">Direct (202) 449-2637</p>
      <div class="divider"></div>
      <p class="email">Email zora@zorafindshomes.example</p>
      <p class="nmls">NMLS #3795038</p>
    </div>
  </article>

</main>
</body>
</html>
```